Creative Businesss Card desgin!

Create a business card for our business Gleam window cleaning!
We are open to creative ideas as long as it maintains a professional image.

Target Market(s)

Small Commercial window cleaning clients including car dealerships, strata manager, cafe

Industry/Entity Type

Window Cleaning

Contact Information for Business Card

Daniel Prescott
General Manager
Gleam Window Cleaning

daniel@gleamservices.com.au
pane-care-southbank.com.au
Ph: 1800 GET GLEAM
Mob: 0437 582 061

Colors
fbed22
0392cd

Requirements
Should not have
• Stock window cleaning/ squeegee graphics

```html
<!DOCTYPE html>
<html lang="en">
<head>
<meta charset="utf-8">
<title>Gleam Window Cleaning – Business Card</title>
<link href="https://fonts.googleapis.com/css2?family=Arimo:wght@700&family=Oswald:wght@400&family=Ubuntu+Condensed&family=Ubuntu:wght@500&display=swap" rel="stylesheet">
<style>
  :root {
    --brand-blue: #265d8a;
    --brand-yellow: #f4ea35;
    --card-white: #ffffff;
    --backdrop: #cfd6d6;
  }
  * { margin: 0; padding: 0; box-sizing: border-box; }
  html, body {
    width: 1200px;
    height: 801px;
    overflow: hidden;
    background: var(--backdrop);
  }
  .card {
    position: absolute;
    left: 382px;
    width: 435px;
    height: 249px;
    overflow: hidden;
  }
  .card--front { top: 106px; background: var(--brand-blue); }
  .card--back  { top: 445px; background: var(--card-white); }
  .card__shapes {
    position: absolute;
    inset: 0;
    width: 100%;
    height: 100%;
  }
  .wordmark {
    position: absolute;
    font-family: "Arimo", Arial, sans-serif;
    font-weight: 700;
    line-height: 1;
  }
  .wordmark__name, .wordmark__tagline { display: block; }
  .card--front .wordmark {
    left: 0; right: 0;
    top: 86px;
    text-align: center;
    color: var(--brand-yellow);
  }
  .card--front .wordmark__name { font-size: 56px; letter-spacing: 1px; }
  .card--front .wordmark__tagline { font-size: 17.5px; margin-top: 6px; }
  .card--back .wordmark {
    left: 23px;
    top: 48px;
    color: var(--brand-blue);
  }
  .card--back .wordmark__name { font-size: 45px; letter-spacing: 1px; }
  .card--back .wordmark__tagline { font-size: 14px; margin-top: 4px; }
  .person {
    position: absolute;
    right: 25px;
    top: 84px;
    text-align: right;
  }
  .person__name {
    font-family: "Oswald", "Arial Narrow", sans-serif;
    font-weight: 400;
    font-size: 30px;
    line-height: 1;
    color: var(--card-white);
    transform: scaleX(0.82);
    transform-origin: right;
    letter-spacing: -0.5px;
  }
  .person__role {
    font-family: "Ubuntu", Arial, sans-serif;
    font-weight: 500;
    font-size: 8px;
    letter-spacing: 0.8px;
    color: var(--brand-yellow);
    margin-top: 1px;
  }
  .contact-list {
    position: absolute;
    right: 29px;
    top: 148px;
    list-style: none;
  }
  .contact-list__item {
    display: flex;
    align-items: center;
    justify-content: flex-end;
    height: 17.7px;
    font-family: "Ubuntu Condensed", "Arial Narrow", sans-serif;
    font-size: 11.5px;
    letter-spacing: -0.2px;
    color: var(--card-white);
  }
  .contact-list__icon {
    width: 9px;
    height: 9px;
    margin-left: 10px;
    fill: var(--card-white);
    flex: none;
  }
</style>
</head>
<body>

<section class="card card--front" aria-label="Business card front">
  <svg class="card__shapes" viewBox="0 0 543 311" preserveAspectRatio="none" aria-hidden="true">
    <polygon points="399,221 482,221 392,311 310,311" fill="var(--brand-yellow)"/>
    <polygon points="543,160 543,311 392,311" fill="var(--card-white)"/>
  </svg>
  <div class="wordmark">
    <span class="wordmark__name">GLEAM</span>
    <span class="wordmark__tagline">WINDOW CLEANING</span>
  </div>
</section>

<section class="card card--back" aria-label="Business card back">
  <svg class="card__shapes" viewBox="0 0 543 311" preserveAspectRatio="none" aria-hidden="true">
    <polygon points="414,0 543,0 543,311 105,311" fill="var(--brand-blue)"/>
    <polygon points="289,56 358,56 105,311 36,311" fill="var(--brand-yellow)"/>
  </svg>
  <div class="wordmark">
    <span class="wordmark__name">GLEAM</span>
    <span class="wordmark__tagline">WINDOW CLEANING</span>
  </div>

  <div class="person">
    <div class="person__name">DANIEL PRESCOTT</div>
    <div class="person__role">General Manager</div>
  </div>

  <ul class="contact-list">
    <li class="contact-list__item">Ph: 1800 GET GLEAM
      <svg class="contact-list__icon" viewBox="0 0 10 10" aria-hidden="true"><path d="M5 0a3.6 3.6 0 0 0-3.6 3.6C1.4 6.3 5 10 5 10s3.6-3.7 3.6-6.4A3.6 3.6 0 0 0 5 0zm0 5.1a1.5 1.5 0 1 1 0-3 1.5 1.5 0 0 1 0 3z"/></svg>
    </li>
    <li class="contact-list__item">0437 582 061
      <svg class="contact-list__icon" viewBox="0 0 10 10" aria-hidden="true"><path d="M2 0.3l1.6 2.3-1 1a6 6 0 0 0 3.8 3.8l1-1L9.7 8 8.6 9.6C4.4 9.8 0.2 5.6 0.4 1.4z"/></svg>
    </li>
    <li class="contact-list__item">pane-care-southbank.com.au
      <svg class="contact-list__icon" viewBox="0 0 10 10" aria-hidden="true"><path d="M0 2h10v6H0zM1 2.8v0.4l4 2.6 4-2.6V2.8L5 5.2z" fill-rule="evenodd"/></svg>
    </li>
    <li class="contact-list__item">daniel@gleamservices.com.au
      <svg class="contact-list__icon" viewBox="0 0 10 10" aria-hidden="true"><path d="M2 0v8.5l2-1.8 1.4 3.2 1.3-.6-1.4-3.1H8z"/></svg>
    </li>
  </ul>
</section>

</body>
</html>
```